Bref créative
business cards and stationary set
vAmu Business cards and stationary
Bright & Fun-filled
Petra Veselinek
Marketing Manager
4127 Marlow Crest Pkwy,
Suite 240
Irving, TX, 75418
petra@vamuleaf.com
www.vamuleaf.com
Logo
picture
picture 2

```html
<!DOCTYPE html>
<html lang="en">
<head>
<meta charset="utf-8">
<title>vAmu Business Card</title>
<link rel="stylesheet" href="https://fonts.googleapis.com/css2?family=Arimo:ital,wght@0,400;0,700;1,400;1,700&display=swap">
<style>
  :root {
    --backdrop: #2b2b2b;
    --card-top: #262626;
    --card-bottom: #0c0c0c;
    --green: #3ee51c;
    --green-dark: #27b80e;
    --white: #ffffff;
    --text-soft: #d8d8d8;
    --ink: #0a0a0a;
  }
  * { box-sizing: border-box; margin: 0; padding: 0; }
  html, body {
    width: 1200px; height: 780px; overflow: hidden;
    background: var(--backdrop);
    font-family: "Arimo", Arial, sans-serif;
  }
  .card {
    position: absolute; left: 75px; top: 90px;
    width: 1050px; height: 600px;
    border-radius: 34px; overflow: hidden;
    background: linear-gradient(160deg, var(--card-top), var(--card-bottom) 70%);
    box-shadow: 0 18px 40px rgba(0,0,0,.55);
  }
  .brand {
    position: absolute; left: 40px; top: 168px; width: 370px; height: 200px;
    text-align: center;
  }
  .brand-rule {
    position: absolute; left: 0; width: 100%; height: 3px;
    background: linear-gradient(90deg, transparent, var(--green) 20%, var(--green) 80%, transparent);
  }
  .brand-rule.top { top: 0; }
  .brand-rule.bottom { bottom: 0; }
  .brand-name {
    position: absolute; left: 0; right: 0; top: 18px;
    font-size: 118px; font-weight: 700; color: var(--white); line-height: 1;
    letter-spacing: -2px;
  }
  .brand-site {
    position: absolute; left: 0; right: 0; top: 146px;
    font-size: 19px; letter-spacing: 8px; color: var(--white);
    text-transform: uppercase;
  }
  .contact { position: absolute; left: 560px; top: 88px; color: var(--text-soft); }
  .person-name { font-size: 36px; font-weight: 700; font-style: italic; color: var(--green); }
  .person-role { font-size: 27px; font-style: italic; color: var(--white); margin-top: 4px; }
  .address { font-size: 24px; line-height: 1.3; margin-top: 40px; }
  .lines { list-style: none; margin-top: 26px; font-size: 23px; }
  .lines li { display: flex; align-items: center; height: 34px; }
  .lines svg { width: 22px; height: 22px; margin-right: 12px; fill: var(--green); }
  .lines .at { width: 22px; margin-right: 12px; color: var(--green); font-weight: 700; text-align: center; }
  .stripe {
    position: absolute; left: 0; right: 0; top: 496px; height: 8px; background: var(--white);
  }
  .band {
    position: absolute; left: 0; right: 0; top: 514px; bottom: 0;
    background: linear-gradient(180deg, var(--green), var(--green-dark));
  }
  .band-site {
    position: absolute; left: 0; width: 700px; top: 550px;
    text-align: center; font-size: 24px; color: var(--ink);
  }
  .badge {
    position: absolute; left: 850px; top: 452px; width: 80px; height: 80px;
    border-radius: 50%; background: var(--white); border: 6px solid var(--ink);
  }
</style>
</head>
<body>
  <div class="card">
    <div class="brand">
      <span class="brand-rule top"></span>
      <div class="brand-name">vAmu</div>
      <div class="brand-site">vamuleaf.com</div>
      <span class="brand-rule bottom"></span>
    </div>

    <div class="contact">
      <div class="person-name">Petra Veselinek</div>
      <div class="person-role">Marketing Manager</div>
      <div class="address">4127 Marlow Crest Pkwy,<br>Suite 240, Irving, TX, 75418</div>
      <ul class="lines">
        <li><svg viewBox="0 0 24 24"><path d="M6.6 10.8a15 15 0 0 0 6.6 6.6l2.2-2.2c.3-.3.7-.4 1-.2 1.1.4 2.3.6 3.6.6.6 0 1 .4 1 1V20c0 .6-.4 1-1 1A17 17 0 0 1 3 4c0-.6.4-1 1-1h3.5c.6 0 1 .4 1 1 0 1.3.2 2.5.6 3.6.1.3 0 .7-.2 1z"/></svg>469-318-2046</li>
        <li><svg viewBox="0 0 24 24"><path d="M7 1h10a2 2 0 0 1 2 2v18a2 2 0 0 1-2 2H7a2 2 0 0 1-2-2V3a2 2 0 0 1 2-2zm0 3v14h10V4zm5 15.5a1.2 1.2 0 1 0 0 2.4 1.2 1.2 0 0 0 0-2.4z"/></svg>214-607-3391</li>
        <li><svg viewBox="0 0 24 24"><path d="M6 2h9l3 3v4H6zM4 10h16a2 2 0 0 1 2 2v6h-4v4H6v-4H2v-6a2 2 0 0 1 2-2zm4 6v4h8v-4z"/></svg>469-318-2098</li>
        <li><span class="at">@</span>petra@vamuleaf.com</li>
      </ul>
    </div>

    <div class="stripe"></div>
    <div class="band"></div>
    <div class="band-site">www.vamuleaf.com</div>
    <div class="badge"></div>
  </div>
</body>
</html>
```